Gravaloop bottle design

We're a small company looking for someone to help with our bottle design. We provide a sauce that will boost the flavor of packaged ramen. We're looking for a label that will stand out. I'm attaching some of the labels we like and some that I've made.

```html
<!DOCTYPE html>
<html lang="en">
<head>
<meta charset="utf-8">
<title>Gravaloop Ramen Sauce Label</title>
<link rel="stylesheet" href="https://fonts.googleapis.com/css2?family=Arimo:wght@700&display=swap">
<style>
  :root {
    --label-red: #ec1c24;
    --pattern-tint: #f4676c;
    --label-white: #ffffff;
    --page-bg: #f4f4f4;
  }
  html, body {
    margin: 0;
    padding: 0;
    width: 1200px;
    height: 1200px;
    overflow: hidden;
    background: var(--page-bg);
  }
  .canvas {
    position: relative;
    width: 1200px;
    height: 1200px;
  }
  .label {
    position: absolute;
    left: 369px;
    top: 80px;
    width: 463px;
    height: 1040px;
  }
  .label-bg { fill: var(--label-red); }
  .pattern-area { fill: var(--pattern-tint); }
  .brand-text {
    font-family: "Arimo", Arial, sans-serif;
    font-weight: 700;
    fill: var(--label-white);
  }
  .brand-stack { font-size: 40px; }
  .brand-tail { font-size: 27px; }
  .product-type { font-size: 11.5px; }
</style>
</head>
<body>
<div class="canvas">
  <svg class="label" viewBox="0 0 190 427" xmlns="http://www.w3.org/2000/svg">
    <rect class="label-bg" width="190" height="427"/>

    <rect class="pattern-area" x="100" y="0" width="90" height="85" role="img" aria-label="White looping noodle-line pattern, top right"/>
    <rect class="pattern-area" x="145" y="100" width="45" height="72" role="img" aria-label="White looping noodle-line pattern, right edge"/>
    <rect class="pattern-area" x="0" y="290" width="36" height="58" role="img" aria-label="White looping noodle-line pattern, left edge"/>
    <rect class="pattern-area" x="0" y="365" width="56" height="62" role="img" aria-label="White looping noodle-line pattern, bottom left"/>

    <g class="brand-text brand-stack" text-anchor="middle">
      <text x="57" y="95">G</text>
      <text x="57" y="147">R</text>
      <text x="57" y="198">A</text>
      <text x="57" y="250">V</text>
      <text x="57" y="301">A</text>
    </g>
    <text class="brand-text brand-stack" x="57" y="353" text-anchor="middle">L</text>
    <text class="brand-text brand-tail" x="78" y="353">OOP</text>
    <text class="brand-text product-type" x="78" y="371">RAMEN SAUCE</text>
  </svg>
</div>
</body>
</html>
```